Dastrelo's New Trucking Company Website

We are wanting to create a basic website for “Dastrelo Trucking” on www.DastreloTrucking.example.

The first attachment titled “write-up” has 7 sections listed, which we would like as tabs at the top of the website, followed by the write up of that section. (The sections ‘employment’ and ‘requirements’ should be under one section).

We would like the landing page to be that of a photo of a Dastrelo Truck. Please see attachment two “Dastrelo_truck” as an example of what our truck looks like. We would like this to be of better quality/more pleasing to the eye. The rest of the attachments (attachment 3- attachment 7) are of possible photos/ideas.

Woould you be able to photoshop any of those trucks to look like our Dastrelo Truck on to a pretty highway/background etc?

We would like this main photo be a constant background of the website, even when you click around the website and the language changes.

Target Market(s)

Northwest Based Companies seeking Transportation needs, grocery stores, Truck Drivers

Industry/Entity Type

Trucking Company

Number of Pages Required

5+ page

Font styles to use
Sans Serif

Requirements
Must have
• Must have one really good photo of our truck (or a truck that looks like ours) as the main photo on the page. This photo must stay consistent as the background when people click on the tabs/sections below.
Nice to have
• Clean/simple layout
Should not have
• Dull colors/ disorganized.

```html
<!DOCTYPE html>
<html lang="en">
<head>
<meta charset="utf-8">
<title>Dastrelo Trucking</title>
<link rel="stylesheet" href="https://fonts.googleapis.com/css2?family=Nunito+Sans:wght@400;600;700&family=Open+Sans:wght@400;600&display=swap">
<style>
:root{
  --teal:#2fc4b7;
  --orange:#ff7b0c;
  --ink:#222;
  --muted:#666;
  --footer:#e9e9e9;
  --white:#fff;
}
*{box-sizing:border-box;margin:0;padding:0}
html,body{width:1200px;height:2553px;overflow:hidden}
body{position:relative;background:var(--white);font-family:"Open Sans",Arial,sans-serif;color:var(--ink)}
.heading{font-family:"Nunito Sans",Arial,sans-serif;font-weight:400}
a{color:inherit;text-decoration:none}

.site-header{position:absolute;left:0;top:0;width:1200px;height:111px}
.brand{position:absolute;left:116px;top:38px;font-family:"Nunito Sans",Arial,sans-serif;font-weight:700;font-size:28px;color:var(--ink);white-space:nowrap}
.main-nav{position:absolute;left:395px;top:45px;display:flex;gap:27px;font-family:"Nunito Sans",Arial,sans-serif;font-size:17px;font-weight:600;color:#222;white-space:nowrap}

.hero{position:absolute;left:0;top:111px;width:1200px;height:599px;
  background:linear-gradient(180deg,#9fb3bf 0%,#6f8592 30%,#2b3438 55%,#3d4a3a 80%,#4b5548 100%)}
.hero-shade{position:absolute;inset:0;background:rgba(0,0,0,.18)}
.hero-title{position:absolute;left:0;width:1200px;top:188px;text-align:center;color:var(--white);font-family:"Nunito Sans",Arial,sans-serif;font-weight:600;font-size:39px;line-height:41px}
.hero-sub{position:absolute;left:0;width:1200px;top:278px;text-align:center;color:#f1f1f1;font-size:18px;line-height:24px}
.hero-btn{position:absolute;left:521px;top:340px;width:150px;height:43px;line-height:43px;text-align:center;background:var(--teal);color:var(--white);font-family:"Nunito Sans",Arial,sans-serif;font-weight:600;font-size:17px;text-transform:uppercase}
.hero-dots{position:absolute;left:555px;top:512px;display:flex;gap:9px}
.hero-dots span{width:15px;height:15px;border-radius:50%;background:var(--white)}
.hero-dots span:first-child{background:transparent;border:2px solid var(--white)}

/* slanted tag buttons */
.tag{position:absolute;display:block;width:136px;height:36px;line-height:36px;padding-left:24px;white-space:nowrap;
  font-family:"Nunito Sans",Arial,sans-serif;font-weight:700;font-size:14px;text-transform:uppercase;color:var(--white);
  clip-path:polygon(0 0,100% 0,calc(100% - 18px) 100%,0 100%)}
.tag-white{background:var(--white);color:#222}
.tag-teal{background:var(--teal)}
.tag-orange{background:var(--orange)}

.about{position:absolute;left:0;top:683px;width:1200px;height:486px}
.about-photo{position:absolute;left:0;top:28px;width:1200px;height:458px;
  background:linear-gradient(120deg,#6b4a2a 0%,#a45a24 35%,#c9772d 55%,#7a5a3a 75%,#5e6a55 100%)}
.about-panel{position:absolute;left:0;top:0;width:755px;height:314px;background:var(--orange);
  clip-path:polygon(0 0,100% 0,587px 100%,0 100%)}
.about-title{position:absolute;left:119px;top:42px;color:var(--white);font-size:31px}
.about-text{position:absolute;left:119px;top:94px;width:490px;color:var(--white);font-size:13.8px;line-height:25px}
.about-btn{left:121px;top:241px}

.cards{position:absolute;left:116px;top:1213px;width:968px;height:360px}
.card{position:absolute;top:0;width:308px;height:341px;border:1px solid #cfcfcf;box-shadow:0 1px 3px rgba(0,0,0,.15);background:var(--white);text-align:center}
.card-photo{height:186px}
.card-title{margin-top:20px;font-family:"Nunito Sans",Arial,sans-serif;font-weight:400;font-size:24px;color:#111}
.card-text{margin:12px auto 0;width:240px;font-size:13px;line-height:20px;color:var(--muted)}
.card-btn{left:88px;top:322px}

.band{position:absolute;left:0;top:1630px;width:1200px;height:360px;
  background:linear-gradient(90deg,#1f4749 0%,#2e5f60 45%,#24504f 70%,#173a3c 100%)}
.band-shade{position:absolute;inset:0;background:rgba(18,52,55,.35)}
.feature{position:absolute;top:103px;width:480px;height:170px}
.feature-icon{position:absolute;left:0;top:0;width:113px;height:113px}
.feature-title{position:absolute;left:125px;top:-6px;color:var(--white);font-size:31px;white-space:nowrap}
.feature-text{position:absolute;left:125px;top:42px;width:350px;color:#e8f1f0;font-size:13.5px;line-height:20px}
.feature-btn{left:125px;top:122px}

.news{position:absolute;left:0;top:1990px;width:1200px;height:418px}
.news-title{position:absolute;left:119px;top:46px;font-size:31px;color:#222}
.post{position:absolute;top:127px;width:310px}
.post-date{color:var(--teal);font-size:17px}
.post-headline{margin-top:12px;font-size:17.5px;line-height:23px;color:#222}
.post-body{margin-top:14px;font-size:12.5px;line-height:21px;color:#444}
.post-more{display:block;margin-top:14px;color:var(--orange);font-size:16.5px;text-transform:uppercase}

.jobs{position:absolute;left:791px;top:2039px;width:300px;height:294px;background:var(--white);box-shadow:0 2px 14px rgba(0,0,0,.22);padding:10px}
.jobs-photo{width:280px;height:210px;background:linear-gradient(135deg,#5c6f7c 0%,#8a9aa4 45%,#b98a6a 70%,#4a5a66 100%)}
.jobs-bar{position:relative;width:280px;height:64px;background:var(--teal);color:var(--white);padding:8px 20px}
.jobs-title{font-family:"Nunito Sans",Arial,sans-serif;font-size:24px;font-weight:400;text-transform:uppercase;line-height:30px}
.jobs-sub{font-size:13px}
.jobs-arrow{position:absolute;right:14px;top:32px}

.site-footer{position:absolute;left:0;top:2408px;width:1200px;height:145px;background:var(--footer)}
.footer-nav{position:absolute;left:126px;top:48px;display:flex;gap:19px;font-size:15px;color:#222;white-space:nowrap}
.copyright{position:absolute;left:126px;top:80px;font-size:12.5px;color:#333}
.social{position:absolute;left:930px;top:44px;display:flex;gap:3px}
.social span{width:32px;height:32px;border:2px solid #222;border-radius:50%}
</style>
</head>
<body>

<header class="site-header">
  <div class="brand">Dastrelo Trucking</div>
  <nav class="main-nav">
    <a href="#">About Us</a><a href="#">Services</a><a href="#">Dispatch</a><a href="#">Equipment</a><a href="#">Safety</a><a href="#">Insurance</a><a href="#">Employment</a>
  </nav>
</header>

<section class="hero" role="img" aria-label="Dastrelo truck driving along a tree-lined highway">
  <div class="hero-shade"></div>
  <h1 class="hero-title">WE PROVIDE TRANSPORTATION<br>AND WAREHOUSING</h1>
  <p class="hero-sub">Morbi diam mauris viverra in gravida eu mattis in ante Morbi eget<br>arcu Morbi porta libero id ullamcorper nonummy</p>
  <a class="hero-btn" href="#">Read More</a>
  <div class="hero-dots"><span></span><span></span><span></span><span></span></div>
</section>

<section class="about">
  <div class="about-photo" role="img" aria-label="Red semi truck with white trailer on a highway among autumn trees"></div>
  <div class="about-panel"></div>
  <h2 class="about-title heading">About Dastrelo Trucking</h2>
  <p class="about-text">Dastrelo Trucking LLC was created in 2012 to assist its parent company, Dastrelo Gourmet, in transporting product from our Seattle HQ to our Portland distribution center every night. Approximately four years later, Dastrelo Trucking has expanded to meet the growing needs of our sister company as well as many Northwest</p>
  <a class="tag tag-white about-btn" href="#">Read More</a>
</section>

<section class="cards">
  <article class="card" style="left:0">
    <div class="card-photo" role="img" aria-label="Truck with box trailer parked under a cloudy sky" style="background:linear-gradient(180deg,#6f7d8e 0%,#9aa6b2 45%,#3d4348 70%,#5a5f55 100%)"></div>
    <h3 class="card-title">OUR SERVICES</h3>
    <p class="card-text">Our mission is to provide the best customer service and trucking services in the Northwest.</p>
    <a class="tag tag-teal card-btn" href="#">Read More</a>
  </article>
  <article class="card" style="left:327px">
    <div class="card-photo" role="img" aria-label="Dark truck on a road through golden grassland at sunset" style="background:linear-gradient(180deg,#d9782e 0%,#a9542a 35%,#4a3a33 60%,#b58a45 100%)"></div>
    <h3 class="card-title">DISPATCH</h3>
    <p class="card-text">Dastrelo Trucking offers refrigerated services in and around Seattle and the Pacific Northwest.</p>
    <a class="tag tag-teal card-btn" href="#">Read More</a>
  </article>
  <article class="card" style="left:660px">
    <div class="card-photo" role="img" aria-label="White truck with trailer on a highway under blue sky" style="background:linear-gradient(180deg,#5a8ac4 0%,#c9d9ea 40%,#e6e9ea 60%,#5f8a4a 80%,#4a7038 100%)"></div>
    <h3 class="card-title">EQUIPMENT</h3>
    <p class="card-text">Dastrelo Trucking provides a variety of transportation, warehousing, consolidating, transportation,</p>
    <a class="tag tag-teal card-btn" href="#">Read More</a>
  </article>
</section>

<section class="band" role="img" aria-label="Truck driver in the cab checking his phone, tinted dark teal">
  <div class="band-shade"></div>
  <div class="feature" style="left:122px">
    <svg class="feature-icon" viewBox="0 0 113 113" fill="none" stroke="#fff" stroke-width="2.5" stroke-linecap="round">
      <circle cx="56.5" cy="56.5" r="55"/>
      <g transform="rotate(45 56.5 56.5)">
        <rect x="49" y="34" width="15" height="36" rx="2"/>
        <line x1="45" y1="34" x2="68" y2="34"/>
        <line x1="56.5" y1="34" x2="56.5" y2="24"/>
        <line x1="50" y1="24" x2="63" y2="24"/>
        <line x1="56.5" y1="70" x2="56.5" y2="88"/>
        <line x1="49" y1="44" x2="55" y2="44"/><line x1="49" y1="52" x2="55" y2="52"/><line x1="49" y1="60" x2="55" y2="60"/>
      </g>
    </svg>
    <h3 class="feature-title heading">Safety</h3>
    <p class="feature-text">Dastrelo Trucking is in full compliance with the Department of Transportation's physical examination and drug testing requirements.</p>
    <a class="tag tag-orange feature-btn" href="#">Read More</a>
  </div>
  <div class="feature" style="left:635px">
    <svg class="feature-icon" viewBox="0 0 113 113" fill="none" stroke="#fff" stroke-width="2.5" stroke-linejoin="round">
      <circle cx="56.5" cy="56.5" r="55"/>
      <rect x="26" y="38" width="38" height="30"/>
      <path d="M64 46h14l10 12v10H64z"/>
      <circle cx="38" cy="72" r="5"/><circle cx="78" cy="72" r="5"/>
      <line x1="18" y1="46" x2="24" y2="46"/><line x1="16" y1="54" x2="24" y2="54"/>
    </svg>
    <h3 class="feature-title heading">Insurance</h3>
    <p class="feature-text">Dastrelo Trucking is fully insured against the risks associated with today's trucking environment and weare an in-bond carrier, as well.</p>
    <a class="tag tag-orange feature-btn" href="#">Read More</a>
  </div>
</section>

<section class="news">
  <h2 class="news-title heading">Latest News</h2>
  <article class="post" style="left:123px">
    <div class="post-date">05 Feb 2016</div>
    <h3 class="post-headline heading">Ut nisi erat fermentum vel congue id euismod in elit Fusce ultrici</h3>
    <p class="post-body">psum cligula augue bibendum accumsan vestibulum ut commodo a mi Morbi ornare gravida elit Integer congue augue et malesuada iaculis</p>
    <a class="post-more" href="#">Read More</a>
  </article>
  <article class="post" style="left:466px">
    <div class="post-date">05 Feb 2016</div>
    <h3 class="post-headline heading">Ut nisi erat fermentum vel congue id euismod in elit Fusce ultrici</h3>
    <p class="post-body">psum cligula augue bibendum accumsan vestibulum ut commodo a mi Morbi ornare gravida elit Integer congue augue et malesuada iaculis</p>
    <a class="post-more" href="#">Read More</a>
  </article>
</section>

<aside class="jobs">
  <div class="jobs-photo" role="img" aria-label="Smiling truck driver at the wheel inside his cab"></div>
  <div class="jobs-bar">
    <div class="jobs-title">Employment</div>
    <div class="jobs-sub">Donec dictum lectus non odio Cras</div>
    <svg class="jobs-arrow" width="18" height="14" viewBox="0 0 18 14" fill="none" stroke="#fff" stroke-width="2"><path d="M1 7h15M10 1l6 6-6 6"/></svg>
  </div>
</aside>

<footer class="site-footer">
  <nav class="footer-nav">
    <a href="#">Home</a><a href="#">About Us</a><a href="#">Services</a><a href="#">Dispatch</a><a href="#">Equipment</a><a href="#">Safety</a><a href="#">Insurance</a><a href="#">Employment</a>
  </nav>
  <p class="copyright">© 2017 Company Name &nbsp;All right reserved &nbsp;Term of Use</p>
  <div class="social" aria-label="Social links"><span></span><span></span><span></span><span></span></div>
</footer>

</body>
</html>
```